FOOD PACKAGING DESIGN

We need a new packaging design for our food product. The product itself is basically dried cheese shreds ( we call it cheese jerky ) which is made from 100% milk. Our product have two flavors: original and spicy. We prefer the new design to be as attractive as possible ( very important ). Like many Japanese food packaging, We like the type of design that makes you feel that it's a premium product and makes you want to try it. Since it is a cheese product, the inclusion of a cute little mouse mascot in the design would be nice but not compulsory. The packaging will be made from Aluminium zip bag with the following size: 26x16 cm (Height x Width).
Attached is our current packaging design, however, we want a whole new refreshing design.

Note: We also attach pictures of our cheese product. Please feel free to modify it according to your creativity. The picture of the product must be different from the original. Do not only 'copy-paste' the picture to your design.

We like elegant design and We want the picture of our product to be "deliciously attractive".

Our product will have the following elements in the packaging:

Front Page:
Product name: CHEESE JERKY. You can play with the font to make it more attractive or playful.
Product net weight ( 2 digits + 'g' ).
A picture of our product.
Flavor Name.
Statement: "No artificial color or preservatives".
Statement: "Please refrigerate after opening".

Back Page:
Area for Product description.
Area for Ingredients list.
Manufacturer information.
Barcode.
Statement: "ISO22000".
Statement: "HACCP".

Reason: Designers submission was very late, need more time to work out with design adjustment.

Reason: Just for finalizing project writing

Target Market(s)

Cheese lovers. Vegetarian. Age group from children to adult. Snack lovers.

Requirements
Must have
• Front Page:
Product net weight.
A picture of our product.
Flavor Name.

Back Page:
Manufacturer information.
Barcode.
Statement: "ISO22000".
Statement: "HACCP".
Nice to have
• Mouse mascot.

```html
<!DOCTYPE html>
<html lang="en">
<head>
<meta charset="utf-8">
<title>Cheese Jerky – Front Pack</title>
<link rel="stylesheet" href="https://fonts.googleapis.com/css2?family=Tinos:wght@400;700&family=Arimo:ital,wght@1,700&family=Roboto+Condensed:wght@400&display=swap">
<style>
  :root {
    --canvas-bg: #e4e4e4;
    --pack-white: #ffffff;
    --pack-red: #e3040b;
    --pack-red-dark: #b80008;
    --pack-red-light: #ff4a4f;
    --leaf-green: #0f7a22;
    --gold-light: #e9c77a;
    --gold-dark: #a8751e;
    --text-white: #ffffff;
    --photo-cream: #fbefc6;
    --photo-yellow: #f2d77a;
    --photo-warm: #e7b98f;
  }
  html, body {
    margin: 0;
    padding: 0;
    width: 1200px;
    height: 1200px;
    overflow: hidden;
    background: var(--canvas-bg);
  }
  .canvas {
    position: relative;
    width: 1200px;
    height: 1200px;
  }
  .pack-art {
    position: absolute;
    inset: 0;
  }
  .product-photo {
    position: absolute;
    left: 300px;
    top: 555px;
    width: 560px;
    height: 350px;
    border-radius: 46% 54% 40% 44% / 50% 50% 42% 46%;
    background:
      radial-gradient(ellipse 55% 50% at 48% 38%, var(--photo-yellow) 0%, var(--photo-cream) 55%, rgba(251,239,198,0) 100%),
      radial-gradient(ellipse 60% 30% at 50% 85%, var(--photo-warm) 0%, rgba(231,185,143,0) 100%);
  }
  .brand-cheese {
    position: absolute;
    left: 338px;
    top: 201px;
    margin: 0;
    font-family: "Tinos", serif;
    font-weight: 400;
    font-size: 82px;
    line-height: 1;
    white-space: nowrap;
    transform: scaleX(0.86);
    transform-origin: left top;
    background: linear-gradient(180deg, var(--gold-light) 0%, var(--gold-dark) 100%);
    -webkit-background-clip: text;
    background-clip: text;
    color: transparent;
  }
  .brand-jerky {
    position: absolute;
    left: 392px;
    top: 261px;
    margin: 0;
    font-family: "Tinos", serif;
    font-weight: 400;
    font-size: 196px;
    line-height: 1;
    white-space: nowrap;
    color: var(--text-white);
    transform: scaleX(0.86);
    transform-origin: left top;
  }
  .flavor-name {
    position: absolute;
    left: 343px;
    top: 491px;
    margin: 0;
    font-family: "Arimo", sans-serif;
    font-style: italic;
    font-weight: 700;
    font-size: 45px;
    line-height: 1;
    white-space: nowrap;
    color: var(--leaf-green);
  }
  .net-weight {
    position: absolute;
    right: 316px;
    top: 939px;
    font-family: "Arimo", sans-serif;
    font-style: italic;
    font-weight: 700;
    font-size: 28px;
    line-height: 1;
    white-space: nowrap;
    color: var(--text-white);
  }
  .claim {
    position: absolute;
    top: 976px;
    font-family: "Roboto Condensed", sans-serif;
    font-size: 20.5px;
    line-height: 1;
    white-space: nowrap;
    color: var(--text-white);
  }
  .claim-natural { left: 304px; }
  .claim-storage { right: 314px; }
</style>
</head>
<body>
<main class="canvas">
  <svg class="pack-art" width="1200" height="1200" viewBox="0 0 1200 1200" aria-hidden="true">
    <defs>
      <clipPath id="pack-outline">
        <rect x="262" y="172" width="676" height="843"/>
      </clipPath>
    </defs>
    <rect class="pack-body" x="262" y="172" width="676" height="843" fill="var(--pack-white)"/>
    <g clip-path="url(#pack-outline)">
      <path class="red-band"
        d="M440,300 C600,292 800,250 945,165 L945,1020 L255,1020 L255,872
           C450,962 700,960 850,900 C935,820 935,620 862,560
           C782,492 600,452 430,446 C372,446 336,412 340,372
           C344,322 390,300 440,300 Z"
        fill="var(--pack-red)" stroke="var(--leaf-green)" stroke-width="26" paint-order="stroke"/>
      <path class="red-heart-shade" d="M440,300 C390,300 344,322 340,372 C337,405 360,432 400,442 C380,420 378,380 400,350 C415,328 430,312 440,300 Z"
        fill="var(--pack-red-light)" opacity="0.5"/>
      <g class="side-stripes" stroke="var(--pack-red-dark)" stroke-width="2" opacity="0.6">
        <line x1="896" y1="190" x2="896" y2="1015"/>
        <line x1="906" y1="186" x2="906" y2="1015"/>
        <line x1="916" y1="182" x2="916" y2="1015"/>
        <line x1="926" y1="178" x2="926" y2="1015"/>
      </g>
      <g class="side-stripes-left" stroke="var(--pack-red)" stroke-width="2" opacity="0.18">
        <line x1="272" y1="200" x2="272" y2="870"/>
        <line x1="282" y1="200" x2="282" y2="875"/>
        <line x1="292" y1="200" x2="292" y2="880"/>
      </g>
    </g>
  </svg>

  <div class="product-photo" role="img" aria-label="Photo of golden dried cheese shreds piled in a white bowl, garnished with a mint leaf and red berries"></div>

  <h1 class="brand-cheese">CHEESE</h1>
  <h2 class="brand-jerky">JERKY</h2>
  <p class="flavor-name">Flavor Name</p>

  <span class="net-weight">net weight XXg</span>
  <span class="claim claim-natural">No artificial color or preservatives</span>
  <span class="claim claim-storage">Please refrigerate after opening</span>
</main>
</body>
</html>
```